Postcard needed for expert witness service

Looking for a professional postcard that will be mailed to personal injury lawyers / law firms to introduce my expert witness services.

Target Market(s)

Law firms, personal injury lawyers

Industry/Entity Type

Expert witness, law

Font styles to use
Sans Serif

Requirements
Must have
• Logo: The Frost Sage [Main Heading]Do you handle snow and ice related slip and falls? Delbert is one of the top snow industry experts in the country! [Following should be in a list type fashion, possibly bulleted]Delbert's credentials: Accredited Winter Technician (AWT), past PRDG board member and chair, former ISO 9001 certified snow company owner , 32 years in the industry. (555) 014-2387 NOTES: Postcard will be 4" x 6" Please use both sides however must have room for labels and stamp
Should not have
• Wouldn't suggest using both photos on same side. Honestly, feel free to only use one of the slip and fall photos if it works out better. Thanks!

```html
<!DOCTYPE html>
<html lang="en">
<head>
<meta charset="utf-8">
<title>The Frost Sage – Postcard</title>
<link href="https://fonts.googleapis.com/css2?family=Roboto:wght@300;400;700;900&display=swap" rel="stylesheet">
<style>
  :root {
    --night: #0d2350;
    --night-deep: #071330;
    --sky: #2a5cae;
    --snow: #e9f0f7;
    --yellow: #fddb35;
    --ink: #1b1b1b;
    --paper: #ffffff;
    --stage: #e8e8e8;
    --rule: #cfcfcf;
    --stamp: #f0f0f0;
  }
  * { box-sizing: border-box; margin: 0; padding: 0; }
  html, body { width: 922px; height: 1200px; overflow: hidden; }
  body { background: var(--stage); font-family: "Roboto", Arial, sans-serif; position: relative; }

  .card { position: absolute; left: 175px; width: 609px; height: 406px; overflow: hidden; }

  /* Front */
  .card-front { top: 135px; background: radial-gradient(ellipse at 50% 60%, var(--sky), var(--night) 60%, var(--night-deep)); }
  .front-scene { position: absolute; inset: 0; }
  .front-photo {
    position: absolute; left: 45px; top: 55px; width: 370px; height: 340px;
    background: linear-gradient(160deg, var(--snow) 0%, #c9d6e6 45%, #8fa6c6 100%);
    clip-path: polygon(8% 12%, 70% 0%, 100% 25%, 92% 60%, 60% 72%, 30% 100%, 4% 86%, 0% 40%);
  }
  .headline {
    position: absolute; left: 42px; top: 50px; padding: 6px 12px 8px;
    border: 2px solid var(--paper); border-radius: 10px;
    transform: rotate(-9deg); transform-origin: left top;
    font-weight: 900; line-height: 1.02; background: rgba(7,19,48,0.25);
  }
  .headline .line-yellow { color: var(--yellow); font-size: 25px; display: block; }
  .headline .line-white { color: var(--paper); font-size: 28px; display: block; }
  .headline .line-small { color: var(--yellow); font-size: 17px; display: block; }

  .front-quote {
    position: absolute; left: 385px; top: 232px; width: 195px;
    color: var(--yellow); font-weight: 700; font-size: 15px; line-height: 1.3; text-align: center;
  }
  .front-quote .mark { position: absolute; right: -12px; top: -12px; font-size: 34px; font-weight: 900; color: var(--paper); line-height: 1; }
  .contact-tag {
    position: absolute; left: 427px; top: 305px; padding: 4px 7px;
    background: var(--yellow); color: var(--night); font-weight: 900; font-size: 15px;
  }
  .contact-tag::after {
    content: ""; position: absolute; left: 12px; bottom: -7px;
    border-left: 7px solid var(--yellow); border-bottom: 7px solid transparent;
  }
  .brand { font-weight: 300; letter-spacing: 1px; text-align: center; }
  .front-brand { position: absolute; left: 405px; top: 347px; width: 180px; color: var(--paper); font-size: 22px; }

  /* Back */
  .card-back { top: 616px; background: var(--paper); }
  .info-panel {
    position: absolute; left: 30px; top: 35px; width: 256px; height: 342px;
    background: var(--yellow); border-radius: 12px; padding: 30px 22px 0;
  }
  .back-quote { position: relative; color: var(--paper); font-weight: 700; font-size: 14.5px; line-height: 1.3; text-align: center; }
  .back-quote .mark { position: absolute; left: -8px; top: -10px; font-size: 30px; font-weight: 900; line-height: 1; }
  .credentials { list-style: none; margin-top: 34px; }
  .credentials li { position: relative; padding-left: 18px; font-size: 11.5px; color: var(--ink); line-height: 1.25; margin-bottom: 10px; }
  .credentials svg { position: absolute; left: 0; top: 2px; }
  .panel-rule { position: absolute; left: 22px; right: 22px; top: 248px; border-top: 1px solid var(--paper); }
  .back-brand { position: absolute; left: 0; right: 0; top: 275px; color: var(--ink); font-size: 22px; }

  .stamp-box { position: absolute; left: 503px; top: 30px; width: 72px; height: 72px; background: var(--stamp); }
  .address-lines { position: absolute; left: 324px; top: 150px; width: 251px; }
  .address-lines span { display: block; border-top: 1px dashed var(--rule); height: 24px; }

  .contact-list { position: absolute; left: 331px; top: 296px; list-style: none; }
  .contact-list li { display: flex; align-items: center; gap: 10px; font-size: 14px; color: var(--ink); height: 27px; }
  .contact-list svg { width: 14px; flex: none; }
</style>
</head>
<body>

<section class="card card-front" aria-label="Postcard front">
  <div class="front-scene" role="img" aria-label="Starry winter night sky behind the scene"></div>
  <div class="front-photo" role="img" aria-label="Photo of a person slipping and falling on snow-covered stairs"></div>

  <h1 class="headline">
    <span class="line-yellow">Do you handle</span>
    <span class="line-white">SNOW and ICE</span>
    <span class="line-small">related slip and falls?</span>
  </h1>

  <p class="front-quote"><span class="mark">&rdquo;</span>Delbert is one of the top snow industry experts in the country</p>
  <div class="contact-tag">CONTACT US</div>
  <div class="brand front-brand">THE FROST SAGE</div>
</section>

<section class="card card-back" aria-label="Postcard back">
  <div class="info-panel">
    <p class="back-quote"><span class="mark">&ldquo;</span>Delbert is one of the top snow industry experts in the country</p>
    <ul class="credentials">
      <li><svg width="10" height="10" viewBox="0 0 10 10"><rect x="0.5" y="0.5" width="9" height="9" fill="none" stroke="#1b1b1b"/><path d="M2 5l2 2 4-5" fill="none" stroke="#1b1b1b" stroke-width="1.2"/></svg>Accredited Winter Technician (AWT)</li>
      <li><svg width="10" height="10" viewBox="0 0 10 10"><rect x="0.5" y="0.5" width="9" height="9" fill="none" stroke="#1b1b1b"/><path d="M2 5l2 2 4-5" fill="none" stroke="#1b1b1b" stroke-width="1.2"/></svg>Past PRDG board member and chair</li>
      <li><svg width="10" height="10" viewBox="0 0 10 10"><rect x="0.5" y="0.5" width="9" height="9" fill="none" stroke="#1b1b1b"/><path d="M2 5l2 2 4-5" fill="none" stroke="#1b1b1b" stroke-width="1.2"/></svg>Former ISO 9001 certified<br>snow company owner</li>
      <li><svg width="10" height="10" viewBox="0 0 10 10"><rect x="0.5" y="0.5" width="9" height="9" fill="none" stroke="#1b1b1b"/><path d="M2 5l2 2 4-5" fill="none" stroke="#1b1b1b" stroke-width="1.2"/></svg>32 years in the industry</li>
    </ul>
    <div class="panel-rule"></div>
    <div class="brand back-brand">THE FROST SAGE</div>
  </div>

  <div class="stamp-box" aria-label="Stamp area"></div>
  <div class="address-lines" aria-label="Address label area">
    <span></span><span></span><span></span><span></span><span></span><span></span>
  </div>

  <ul class="contact-list">
    <li><svg viewBox="0 0 14 18"><path d="M7 0a6 6 0 0 0-6 6c0 5 6 12 6 12s6-7 6-12a6 6 0 0 0-6-6zm0 8.5A2.5 2.5 0 1 1 7 3.5a2.5 2.5 0 0 1 0 5z" fill="#fddb35"/></svg>thefrostsage.com</li>
    <li><svg viewBox="0 0 14 14"><path d="M3 0l3 3-2 2c1 2 3 4 5 5l2-2 3 3-2 3C6 14 0 8 0 3z" fill="#fddb35"/></svg>(555) 014-2387</li>
    <li><svg viewBox="0 0 14 10"><rect width="14" height="10" fill="#fddb35"/><path d="M0 0l7 6 7-6" fill="none" stroke="#fff" stroke-width="1.2"/></svg>info@thefrostsage.com</li>
  </ul>
</section>

</body>
</html>
```